TQRVA Membership Flyer

• 1 Page Flyer promoting TQRVA Membership Drive
• I have attached our organization brochure for organizational info
• Please include the same TQRVA logo as seen in brochure
• Membership $20/year
• Contact Milo Banter to Join at banmil42@learners.fpx.edu
INCLUDE Organization Advisers
Dr. Torvald Penning FPX School of Dental Medicine (photo from attached brochure)
Dr. Felix Ormond FPX Talwick School of Medicine (Photo from Attached brochure)

Member Benefits
• Access to exclusive Interdisciplinary world-renowned guest speaker presentations
• Mentorship for residencies / Oral Medicine Fellowship for nondental healthcare students
• Shadowing opportunities with Oral Medicine Specialist
• Participate in research journal club
• Clinical Research, Case Reports and Lindqvart Fellowship opportunities
• Exclusive Lunch and Learn Invitations
• 10% Discount to Special Events Sponsored by TQRVA
• Enhance your Interdisciplinary resource network

Renew or Join TQRVA by August 30th and be entered in a free raffle for the chance to win one of 3 drawings
$50 Pavex Gift Card
2x $25 Brewmoor Gift Card

Target Market(s)

Students

Requirements
Must have
• Must use the TQRVA Logo from brochure, Member Benefits • Access to exclusive Interdisciplinary world-renowned guest speaker presentations • Mentorship for residencies / Oral Medicine Fellowship for nondental healthcare students • Shadowing opportunities with Oral Medicine Specialist • Participate in research journal club • Clinical Research, Case Reports and Lindqvart Fellowship opportunities • Exclusive Lunch and Learn Invitations • 10% Discount to Special Events Sponsored by TQRVA • Enhance your Interdisciplinary resource network Renew or Join TQRVA by August 30th and be entered in a free raffle for the chance to win one of 3-4 drawings $50 Pavex Gift Card 2x $25 Brewmoor Gift Card
Nice to have
• Similar design background to brochure attached,

```html
<!DOCTYPE html>
<html lang="en">
<head>
<meta charset="utf-8">
<title>TQRVA Membership Flyer</title>
<link href="https://fonts.googleapis.com/css2?family=Montserrat:wght@400;600;700&family=Oswald:wght@600;700&family=Lato:wght@400&display=swap" rel="stylesheet">
<style>
:root{
  --purple:#5f3591;
  --purple-light:#673a95;
  --purple-dark:#46236a;
  --gold:#cdb35c;
  --paper:#e9e9ea;
  --ink:#333336;
  --stage:#dcdcdc;
  --white:#ffffff;
}
*{margin:0;padding:0;box-sizing:border-box}
html,body{width:1200px;height:1200px;overflow:hidden;background:var(--stage)}
.canvas{position:relative;width:1200px;height:1200px}
.flyer{position:absolute;left:160px;top:34px;width:1223px;height:1573px;transform:scale(0.72);transform-origin:0 0;background:var(--paper);overflow:hidden;font-family:'Montserrat',sans-serif;color:var(--ink)}
.backdrop{position:absolute;inset:0}
.abs{position:absolute}
.brand{left:90px;top:70px;color:var(--purple);font-family:'Montserrat',sans-serif;font-weight:600;text-align:center;line-height:1;font-size:92px;letter-spacing:2px}
.brand span{display:block;margin-bottom:10px}
.advisers-title{left:679px;top:34px;font-size:26px;font-weight:600;color:var(--purple);letter-spacing:.5px}
.advisers-rule{left:993px;top:52px;width:130px;height:3px;background:var(--purple-dark)}
.portrait{background:linear-gradient(180deg,#9a9aa0,#5d5f68);border:2px solid var(--purple)}
.adviser{font-size:15px;line-height:20px;color:var(--ink);white-space:nowrap}
.adviser b{display:block;font-weight:700;color:var(--ink);letter-spacing:-.3px}
.pill{left:0;height:47px;padding:0 28px 0 34px;background:var(--purple);color:var(--white);border-radius:0 24px 24px 0;font-size:32px;font-weight:600;line-height:47px}
.copy{left:34px;width:480px;font-size:22px;line-height:28px}
.copy p{margin-bottom:7px}
.benefits{left:38px;top:820px;list-style:none;width:820px;font-size:21px;line-height:28px}
.benefits li{position:relative;padding-left:21px;margin-bottom:18px}
.benefits li::before{content:"";position:absolute;left:0;top:9px;width:11px;height:11px;border-radius:50%;background:var(--gold)}
.raffle{left:547px;top:318px;width:600px;text-align:center;color:var(--white)}
.raffle-intro{font-size:24px;line-height:32px;font-weight:400;white-space:nowrap}
.prize{font-family:'Oswald',sans-serif;font-weight:700;font-size:62px;line-height:70px}
.prize-main{margin-top:10px}
.prize-second{margin-top:78px}
.cta{left:209px;top:1308px;font-family:'Oswald',sans-serif;font-weight:700;font-size:62px;color:var(--purple);letter-spacing:.5px}
.contact{left:219px;top:1388px;font-family:'Lato',sans-serif;font-size:30px;line-height:47px;color:#1f1f22}
.model{left:850px;top:865px;width:332px;height:672px;background:linear-gradient(180deg,#d9d9dc 0%,#f6f6f7 45%,#eeeef0 100%);border-radius:150px 150px 0 0}
</style>
</head>
<body>
<div class="canvas">
  <article class="flyer">
    <svg class="backdrop" viewBox="0 0 1223 1573" width="1223" height="1573" aria-hidden="true">
      <defs>
        <clipPath id="raffle-disc"><circle cx="847" cy="505" r="300"/></clipPath>
      </defs>
      <polygon points="819,0 1223,0 1223,195 1097,305 707,225" fill="var(--gold)"/>
      <polygon points="1142,625 1223,685 1223,1265 827,820" fill="var(--gold)"/>
      <polygon points="0,1250 200,1410 0,1530" fill="var(--gold)"/>
      <rect x="0" y="1537" width="1223" height="36" fill="var(--purple)"/>
      <circle cx="847" cy="505" r="313" fill="var(--white)"/>
      <g clip-path="url(#raffle-disc)">
        <rect x="540" y="200" width="620" height="360" fill="var(--purple-light)"/>
        <rect x="540" y="560" width="620" height="260" fill="var(--purple-dark)"/>
      </g>
    </svg>

    <div class="abs brand"><span>FPX</span><span>TQRVA</span></div>

    <div class="abs advisers-title">Organization Advisers</div>
    <div class="abs advisers-rule"></div>
    <div class="abs portrait" style="left:668px;top:76px;width:78px;height:101px" role="img" aria-label="Portrait photo of Dr. Torvald Penning"></div>
    <div class="abs adviser" style="left:755px;top:92px"><b>Dr. Torvald Penning</b>FPX School of<br>Dental Medicine</div>
    <div class="abs portrait" style="left:940px;top:73px;width:78px;height:104px" role="img" aria-label="Portrait photo of Dr. Felix Ormond"></div>
    <div class="abs adviser" style="left:1027px;top:94px"><b>Dr. Felix Ormond</b>FPX Talwick School<br>of Medicine</div>

    <div class="abs pill" style="top:308px">Vision</div>
    <div class="abs copy" style="top:360px"><p>Integration of all healthcare schools at FPX to promote collaborative and optimal patient care.</p></div>

    <div class="abs pill" style="top:463px">Mission</div>
    <div class="abs copy" style="top:519px;width:500px">
      <p>Increase professional awareness of the field of Oral Medicine.</p>
      <p>Create a platform for shared learning between healthcare schools of FPX.</p>
      <p>Provide opportunity for mentoring and career counseling in Oral Medicine for all healthcare students.</p>
    </div>

    <div class="abs pill" style="top:754px">Benefits</div>
    <ul class="abs benefits">
      <li>Access to exclusive Interdisciplinary world-renowned guest<br>speaker presentations</li>
      <li>Mentorship for residencies / Oral Medicine Fellowship for nondental<br>healthcare students</li>
      <li>Shadowing opportunities with Oral Medicine Specialist</li>
      <li>Participate in research journal club</li>
      <li>Clinical Research, Case Reports and Lindqvart Fellowship opportunities</li>
      <li>Exclusive Lunch and Learn Invitations</li>
      <li>10% Discount to Special Events Sponsored by TQRVA</li>
      <li>Enhance your Interdisciplinary resource network</li>
    </ul>

    <div class="abs raffle">
      <p class="raffle-intro">Renew or Join TQRVA by August<br>30th and be entered in a free<br>raffle for the chance to win one of<br>3 drawings</p>
      <p class="prize prize-main">$50 Pavex Gift Card</p>
      <p class="prize prize-second">2x $25 Brewmoor<br>Gift Card</p>
    </div>

    <div class="abs model" role="img" aria-label="Photo of a young doctor in a white coat with arms crossed"></div>

    <h2 class="abs cta">INTERESTED IN JOINING?</h2>
    <div class="abs contact">Contact: Milo Banter<br>Email: banmil42@learners.fpx.edu</div>
  </article>
</div>
</body>
</html>
```